Trucking Insurance Website Design

We are working with a Trucking Insurance company in California. They provide vehicle insurance for trucking companies and truckers.
As you might imagine, there are no websites we could find for inspiration for trucking insurance. But below are sites that do similar insurance.
https://brindlemorecover.com/trucking-insurance/
https://www.haulwardpolicy.com/california-commercial-truck-insurance
Thank you for taking the time to consider designing a website for us. We are web developers based in Stockton, CA, USA. Most of our projects go through the same process. Understanding this process may help you win a project with us. We custom-code all of our websites in-house. We don’t have any requirements as to what tools you use for your design, but we ask that you follow these guidelines.
IMAGES:
If you use any images or icons in the design, we ask that you have a link to the asset so we can purchase the image/icon. Most of the designs we submit do not have the customer’s images on them unless they have some great images. Be creative; show us the feeling you are trying to portray with your image choices. Use any royalty-free site you choose. We subscribe to Quillen and mainly use their images, but we can purchase images outside of Quillen. PLEASE NOTE: we will not submit designs to clients with watermarks on the images.
FONTS:
We ask that you identify the fonts you’re using in the design. This can be done in a message if you want. We typically use Marlowe Type and Quillen Type.
CONTENT:
We're always open to different content and ideas. We often submit designs with stock images so the client can see our vision. We typically take pictures after the website launch to use their images with our vision. Lorem Ipsum is fine for paragraphs, but we ask that you make the Headers with correct English. We want to be able to show the vision and identify the sections of the website.
INSPIRATION:
We typically add a couple of links in the brief of websites we like to help you get started in your design.
REVISIONS:
We do not often ask for revisions of the designs unless we see something in the design that may not appeal to the client. If there are slight changes that we want to make, we do that in the development process.
FEEDBACK:
We rarely give feedback on designs during the design process. We are working on many website projects and do not have the time to provide feedback. We usually respond if your request is well thought out and asks specific questions, but a note asking “feedback, please” usually goes unanswered.
1 page

```html
<!DOCTYPE html>
<html lang="en">
<head>
<meta charset="utf-8">
<title>Roadstead Insurance – Trucking Insurance</title>
<link rel="stylesheet" href="https://fonts.googleapis.com/css2?family=Poppins:wght@400;500;600;700;800&family=Arimo:wght@400;700&display=swap">
<style>
:root{
  --red:#c0181f;
  --blue:#6478c6;
  --ink:#2a2a2a;
  --grey-bg:#f4f4f4;
  --muted:#6a6a6a;
  --footer:#1b1b1b;
  --white:#fff;
}
*{margin:0;padding:0;box-sizing:border-box}
html,body{width:1200px;height:3987px;overflow:hidden;background:#fff}
body{position:relative;font-family:Arimo,Arial,sans-serif;color:var(--ink)}
.abs{position:absolute}
.heading{font-family:Poppins,sans-serif;font-weight:700;text-transform:uppercase;text-align:center;color:var(--ink);line-height:1.1}
.outline{font-family:Poppins,sans-serif;font-weight:700;text-transform:uppercase;color:transparent;-webkit-text-stroke:2px var(--ink);text-align:center;line-height:1.1;letter-spacing:-1px}
.btn{position:absolute;border-radius:20px;font-family:Arimo,sans-serif;font-weight:700;font-size:12px;display:flex;align-items:center;justify-content:center}
.btn-red{background:var(--red);color:#fff}
.btn-white{background:#fff;color:var(--blue)}
.photo{position:absolute}

/* top bar */
.topbar{left:100px;top:25px;width:1002px;height:32px;background:var(--red)}
.social-dot{position:absolute;top:7px;width:18px;height:18px;border-radius:50%;background:#fff}
.call{position:absolute;right:120px;top:8px;color:#fff;font-size:11px;display:flex;align-items:center;gap:8px}
.call .ring{width:18px;height:18px;border-radius:50%;background:#fff;display:flex;align-items:center;justify-content:center}

/* nav */
.logo-disc{left:176px;top:57px;width:208px;height:129px;background:#fff;border-radius:0 0 104px 104px;z-index:3}
.wordmark{display:flex;align-items:center;gap:8px;font-family:Poppins,sans-serif;font-weight:600;white-space:nowrap}
.wordmark .dot{width:12px;height:12px;border-radius:50%;background:var(--red);flex:none}
.logo-disc .wordmark{position:absolute;left:0;width:100%;top:40px;justify-content:center;font-size:14px;color:var(--ink)}
.nav{left:494px;top:86px;display:flex;gap:22px;font-size:11px;color:#333}
.nav .active{color:var(--red);border-bottom:1px solid var(--red);padding-bottom:4px}
.quote{left:845px;top:79px;width:136px;height:31px;font-size:12px}

/* hero */
.hero{left:100px;top:130px;width:1002px;height:536px;background:linear-gradient(180deg,#7f93b3 0%,#b7b4ad 40%,#5a5a55 58%,#202024 100%)}
.hero-title{left:217px;top:428px;font-family:Poppins,sans-serif;font-weight:800;font-size:60px;color:#fff;line-height:1}
.hero-outline{left:215px;top:496px;font-family:Poppins,sans-serif;font-weight:700;font-size:82px;color:transparent;-webkit-text-stroke:2px #fff;line-height:1;letter-spacing:-1px}
.hero-arrow{top:544px;width:31px;height:31px;border-radius:50%;background:rgba(90,90,90,.8);display:flex;align-items:center;justify-content:center}

/* intro */
.intro-h{left:0;width:1200px;top:754px;font-size:30px}
.intro-p{left:220px;top:840px;width:764px;font-size:11px;line-height:20px;text-align:center;color:var(--muted)}

/* mission */
.mission-bg{left:100px;top:1101px;width:1002px;height:467px;background:var(--grey-bg)}
.mission-panel{left:604px;top:1300px;width:379px;height:378px;background:var(--blue);color:#fff;padding:36px 26px 0 25px;font-size:10.5px;line-height:23.3px}
.mission-panel p{text-align:justify}

/* cards */
.card{position:absolute;top:1877px;width:231px;height:338px;border:1px solid #e2e2e2;background:#fff}
.card .photo{left:0;top:0;width:229px;height:180px}
.card h3{position:absolute;top:200px;width:100%;text-align:center;font-family:Arimo,sans-serif;font-size:16px;font-weight:700;color:#222}
.card p{position:absolute;top:231px;left:22px;right:22px;font-size:10.5px;line-height:20px;text-align:center;color:var(--muted)}
.card-arrow{position:absolute;top:2203px;width:34px;height:34px;background:var(--red);display:flex;align-items:center;justify-content:center}

/* links */
.links-bg{left:100px;top:2329px;width:1002px;height:641px;background:var(--red)}
.links-p{left:200px;top:2476px;width:800px;font-size:10.5px;line-height:19px;text-align:center;color:#fff}
.link-label{position:absolute;top:2806px;width:280px;height:52px;background:#fff;color:var(--red);font-weight:700;font-size:16px;display:flex;align-items:center;justify-content:center}

/* cta band */
.cta{left:0;top:3549px;width:1200px;height:70px}
.cta-text{left:0;width:1200px;top:3570px;display:flex;justify-content:center;align-items:center;gap:12px;color:#fff;font-size:13px;font-family:Arimo,sans-serif}
.cta-text b{font-weight:700}

/* footer */
.footer{left:100px;top:3619px;width:1002px;height:356px;background:var(--footer);color:#aaa;font-size:11px}
.footer .wordmark{position:absolute;left:117px;top:128px;font-size:16px;color:#fff}
.footer .wordmark .dot{width:14px;height:14px}
.f-h{position:absolute;top:74px;font-family:Poppins,sans-serif;font-weight:600;font-size:16px;color:#fff}
.f-h::after{content:"";position:absolute;left:0;top:28px;width:16px;height:2px;background:var(--red)}
.f-list{position:absolute;list-style:none;line-height:20px;color:#999;font-size:11px}
.f-list li::before{content:"»";margin-right:14px;color:#888}
</style>
</head>
<body>

<!-- top bar -->
<div class="abs topbar">
  <span class="social-dot" style="left:121px"></span>
  <span class="social-dot" style="left:147px"></span>
  <span class="social-dot" style="left:174px"></span>
  <div class="call"><span class="ring"><svg width="10" height="10" viewBox="0 0 24 24"><path fill="#c0181f" d="M6.6 10.8a15.1 15.1 0 0 0 6.6 6.6l2.2-2.2c.3-.3.7-.4 1-.2 1.1.4 2.3.6 3.6.6.6 0 1 .4 1 1V20c0 .6-.4 1-1 1A17 17 0 0 1 3 4c0-.6.4-1 1-1h3.5c.6 0 1 .4 1 1 0 1.3.2 2.5.6 3.6.1.3 0 .7-.2 1z"/></svg></span>Call Us : +1 888 888 8888</div>
</div>

<!-- logo disc -->
<div class="abs logo-disc">
  <div class="wordmark"><span class="dot"></span>Roadstead Insurance</div>
</div>

<!-- nav -->
<nav class="abs nav">
  <span class="active">Home</span><span>About</span><span>Trucking</span><span>Personal</span><span>Business</span><span>Benefits</span>
</nav>
<div class="btn btn-red quote">Request A Quote</div>

<!-- hero -->
<div class="abs hero" role="img" aria-label="Semi truck driving on a highway at sunset"></div>
<div class="abs hero-title">ROADSTEAD</div>
<div class="abs hero-outline">INSURANCE</div>
<div class="abs hero-arrow" style="left:894px"><svg width="10" height="10" viewBox="0 0 10 10"><path d="M6.5 2 3.5 5l3 3" stroke="#fff" stroke-width="1.4" fill="none"/></svg></div>
<div class="abs hero-arrow" style="left:934px"><svg width="10" height="10" viewBox="0 0 10 10"><path d="M3.5 2l3 3-3 3" stroke="#fff" stroke-width="1.4" fill="none"/></svg></div>

<!-- intro -->
<h2 class="abs heading intro-h">There’s a long road ahead,<br>and we are with you all the way.</h2>
<p class="abs intro-p">Lorem ipsum dolor sit amet, consectetur adipiscing elit, sed do eiusmod tempor incididunt ut labore et dolore magna aliqua. Ut enim ad minim veniam, quis nostrud exercitation ullamco laboris nisi ut aliquip ex ea commodo consequat. Duis aute irure dolor in reprehenderit in voluptate velit esse cillum dolore eu fugiat nulla pariatur. Excepteur sint occaecat cupidatat non proident, sunt in culpa qui officia deserunt mollit anim id est laborum. Lorem ipsum dolor sit amet, consectetur adipiscing elit, sed do eiusmod tempor incididunt ut labore et dolore magna aliqua. Ut enim ad minim veniam, quis nostrud exercitation ullamco laboris nisi ut aliquip ex ea commodo consequat. Duis aute irure dolor in reprehenderit in voluptate velit esse cillum dolore eu fugiat nulla pariatur. Excepteur sint occaecat cupidatat non proident, sunt in culpa qui officia deserunt mollit anim id est laborum.</p>
<div class="btn btn-red" style="left:535px;top:975px;width:136px;height:33px">Learn More</div>

<!-- mission -->
<div class="abs mission-bg"></div>
<div class="abs heading" style="left:0;width:1200px;top:1187px;font-size:30px">Our Trucking</div>
<div class="abs outline" style="left:0;width:1200px;top:1224px;font-size:46px">Service Mission</div>
<div class="photo" style="left:100px;top:1300px;width:504px;height:378px;background:linear-gradient(160deg,#7d9a55 0%,#4f6a3a 45%,#8a8d88 75%,#5d6168 100%)" role="img" aria-label="Two trucks on a curving highway seen from above"></div>
<div class="abs mission-panel">
  <p>Lorem ipsum dolor sit amet, consectetur adipiscing elit, sed do eiusmod tempor incididunt ut labore et dolore magna aliqua. Ut enim ad minim veniam, quis nostrud exercitation ullamco laboris nisi ut aliquip ex ea commodo consequat. Duis aute irure dolor in reprehenderit in voluptate velit esse cillum dolore eu fugiat nulla pariatur.</p>
  <p style="margin-top:23px">Excepteur sint occaecat cupidatat non proident, sunt in culpa qui officia deserunt mollit anim id est laborum. Lorem ipsum dolor sit amet, consectetur adipiscing elit, sed do eiusmod tempor incididunt ut labore et dolore magna aliqua.</p>
</div>
<div class="btn btn-white" style="left:629px;top:1608px;width:134px;height:32px">Learn More</div>

<!-- specialization -->
<div class="abs heading" style="left:0;width:1200px;top:1762px;font-size:30px">Industry</div>
<div class="abs outline" style="left:0;width:1200px;top:1800px;font-size:46px">Specialization</div>

<div class="card" style="left:222px">
  <div class="photo" style="background:linear-gradient(180deg,#9dbbd6 0%,#c2c6cb 55%,#8f9499 100%)" role="img" aria-label="Truck parked at a warehouse loading dock"></div>
  <h3>Risk Management</h3>
  <p>Lorem ipsum dolor sit amet, conse ctetur adipiscing elit, sed do eius mod tempor incididunt ut labore et dolore magna aliqua.</p>
</div>
<div class="card" style="left:486px">
  <div class="photo" style="background:linear-gradient(160deg,#2c3a44 0%,#b8582a 40%,#3d6b73 70%,#1d2328 100%)" role="img" aria-label="Truck speeding through a lit tunnel"></div>
  <h3>Products</h3>
  <p>Lorem ipsum dolor sit amet, conse ctetur adipiscing elit, sed do eius mod tempor incididunt ut labore et dolore magna aliqua.</p>
</div>
<div class="card" style="left:751px">
  <div class="photo" style="background:linear-gradient(180deg,#7c8792 0%,#c9ccd0 50%,#5d6166 100%)" role="img" aria-label="Row of white delivery vans at a depot"></div>
  <h3>Options</h3>
  <p>Lorem ipsum dolor sit amet, conse ctetur adipiscing elit, sed do eius mod tempor incididunt ut labore et dolore magna aliqua.</p>
</div>
<div class="card-arrow" style="left:319px"><svg width="11" height="11" viewBox="0 0 12 12"><path d="M1 6h9M6.5 2.5 10 6l-3.5 3.5" stroke="#fff" stroke-width="2" fill="none"/></svg></div>
<div class="card-arrow" style="left:584px"><svg width="11" height="11" viewBox="0 0 12 12"><path d="M1 6h9M6.5 2.5 10 6l-3.5 3.5" stroke="#fff" stroke-width="2" fill="none"/></svg></div>
<div class="card-arrow" style="left:849px"><svg width="11" height="11" viewBox="0 0 12 12"><path d="M1 6h9M6.5 2.5 10 6l-3.5 3.5" stroke="#fff" stroke-width="2" fill="none"/></svg></div>

<!-- industry links -->
<div class="abs links-bg"></div>
<div class="abs outline" style="left:0;width:1200px;top:2404px;font-size:46px;-webkit-text-stroke:2px #fff">Trucking Industry Links</div>
<p class="abs links-p">Lorem ipsum dolor sit amet, consectetur adipiscing elit, sed do eiusmod tempor incididunt ut labore et dolore magna aliqua. Ut enim ad minim veniam, quis nostrud exercitation ullamco laboris nisi ut aliquip ex ea commodo consequat.</p>
<div class="photo" style="left:222px;top:2534px;width:365px;height:301px;background:linear-gradient(170deg,#cfd6dd 0%,#b0283a 45%,#6e1622 80%,#3a3a3a 100%)" role="img" aria-label="Red semi truck cab close-up"></div>
<div class="photo" style="left:618px;top:2534px;width:365px;height:301px;background:linear-gradient(180deg,#6e747b 0%,#dfe2e5 50%,#8a8e93 100%)" role="img" aria-label="Two white trucks parked side by side"></div>
<div class="link-label" style="left:264px">Lorem ipsum dolor sit</div>
<div class="link-label" style="left:661px">Lorem ipsum dolor sit</div>
<svg class="abs" style="left:146px;top:2672px" width="28" height="22" viewBox="0 0 28 22"><path d="M26 11H3M12 2 3 11l9 9" stroke="#fff" stroke-width="2.5" fill="none"/></svg>
<svg class="abs" style="left:1029px;top:2672px" width="28" height="22" viewBox="0 0 28 22"><path d="M2 11h23M16 2l9 9-9 9" stroke="#fff" stroke-width="2.5" fill="none"/></svg>

<!-- more than price -->
<div class="abs heading" style="left:0;width:1200px;top:3056px;font-size:30px">There’s more to insurance than</div>
<div class="abs outline" style="left:0;width:1200px;top:3092px;font-size:48px">The price of the policy</div>
<div class="photo" style="left:248px;top:3183px;width:715px;height:310px;background:radial-gradient(ellipse at 50% 60%,#d9dadc 0%,#eeeff0 45%,#ffffff 72%)" role="img" aria-label="Fleet of white semi trucks arranged in a V formation"></div>

<!-- call band -->
<svg class="abs cta" width="1200" height="70" viewBox="0 0 1200 70"><path d="M342 0H862L913 70H292Z" fill="#6478c6"/></svg>
<div class="abs cta-text">
  <span>THE NEXT STEP IS EASY</span>
  <span style="width:24px;height:24px;border-radius:50%;background:#fff;display:flex;align-items:center;justify-content:center"><svg width="12" height="12" viewBox="0 0 24 24"><path fill="#6478c6" d="M6.6 10.8a15.1 15.1 0 0 0 6.6 6.6l2.2-2.2c.3-.3.7-.4 1-.2 1.1.4 2.3.6 3.6.6.6 0 1 .4 1 1V20c0 .6-.4 1-1 1A17 17 0 0 1 3 4c0-.6.4-1 1-1h3.5c.6 0 1 .4 1 1 0 1.3.2 2.5.6 3.6.1.3 0 .7-.2 1z"/></svg></span>
  <b>CALL : +1 888 888 8888</b>
</div>

<!-- footer -->
<footer class="abs footer">
  <div class="wordmark"><span class="dot"></span>Roadstead Insurance</div>
  <p style="position:absolute;left:117px;top:198px;width:235px;line-height:19px;color:#999">Lorem ipsum dolor sit amet, consectetur adi pisci ng elit, sed do eiusmod</p>

  <div class="f-h" style="left:386px">Office</div>
  <svg style="position:absolute;left:386px;top:128px" width="9" height="12" viewBox="0 0 10 14"><path fill="#888" d="M5 0a5 5 0 0 0-5 5c0 4 5 9 5 9s5-5 5-9a5 5 0 0 0-5-5zm0 7a2 2 0 1 1 0-4 2 2 0 0 1 0 4z"/></svg>
  <p style="position:absolute;left:414px;top:124px;width:150px;line-height:20px;color:#999">Lorem ipsum dolor sit amet, consectetur adi</p>
  <svg style="position:absolute;left:385px;top:183px" width="11" height="8" viewBox="0 0 12 9"><rect width="12" height="9" fill="#888"/><path d="M0 0l6 5 6-5" stroke="#1b1b1b" fill="none"/></svg>
  <p style="position:absolute;left:414px;top:179px;color:#bbb;text-decoration:underline">info@companyname.com</p>
  <svg style="position:absolute;left:386px;top:221px" width="10" height="10" viewBox="0 0 24 24"><path fill="#888" d="M6.6 10.8a15.1 15.1 0 0 0 6.6 6.6l2.2-2.2c.3-.3.7-.4 1-.2 1.1.4 2.3.6 3.6.6.6 0 1 .4 1 1V20c0 .6-.4 1-1 1A17 17 0 0 1 3 4c0-.6.4-1 1-1h3.5c.6 0 1 .4 1 1 0 1.3.2 2.5.6 3.6.1.3 0 .7-.2 1z"/></svg>
  <p style="position:absolute;left:414px;top:218px;color:#999">+1 888 888 8888</p>

  <div class="f-h" style="left:586px">Links</div>
  <ul class="f-list" style="left:586px;top:124px">
    <li>Home</li><li>About</li><li>Mission</li><li>Service</li><li>Blog</li><li>Contact</li>
  </ul>

  <div class="f-h" style="left:726px">Newsletter</div>
  <div style="position:absolute;left:728px;top:120px;width:112px;border-bottom:1px solid #666;padding-bottom:6px;font-size:8px;color:#999">✉ Email address</div>
  <div class="btn btn-red" style="left:728px;top:148px;width:86px;height:25px;font-size:8px">SUBMIT</div>
  <span style="position:absolute;left:730px;top:218px;width:10px;height:10px;border-radius:50%;background:#ddd"></span>
  <span style="position:absolute;left:754px;top:218px;width:10px;height:10px;border-radius:50%;background:#ddd"></span>
  <span style="position:absolute;left:778px;top:218px;width:10px;height:10px;border-radius:50%;background:#ddd"></span>
  <span style="position:absolute;left:802px;top:218px;width:10px;height:10px;border-radius:50%;background:#ddd"></span>

  <p style="position:absolute;left:0;width:100%;top:292px;text-align:center;color:#999">© Copyrights 2023 | All Rights Reserved</p>
</footer>

</body>
</html>
```